New design for our website – modern, elegant, and customer-focused

We want to redesign our website, www.kalmenstrand.se, to create a completely new look that reflects the high quality of our products and services. We are seeking assistance in developing a modern, clean, and user-friendly web experience in Flatsome that strengthens our brand and makes it easier for customers to find the right solutions. Our goal is to enhance the design, functionality, and overall impression to better meet today’s expectations and demands.

Target Market(s)

swimmingpool & spa

Industry/Entity Type

Poolbusiness

Coding

Coded - Design and coding required

Number of Pages Required

1 page

Font styles to use
Other font styles liked:
• HaboroSoft

Requirements
Must have
• We working in Flatsome
Nice to have
• From dream to reality – swimming pools that transform your garden into a place of life and enjoyment.
Should not have
• Nice look

```html
<!DOCTYPE html>
<html lang="sv">
<head>
<meta charset="utf-8">
<title>Kalmenstrand – Pooler som förvandlar din trädgård</title>
<link href="https://fonts.googleapis.com/css2?family=Playfair+Display:wght@600;700&family=Inter:wght@400;500;600&display=swap" rel="stylesheet">
<style>
:root{
  --ink:#1f2a37;
  --muted:#5b6b7d;
  --blue:#0a7fc0;
  --blue-dark:#0b5a8c;
  --cyan:#14b8d4;
  --line:#e4ebf2;
  --bg:#ffffff;
  --soft:#f7fafc;
  --footer:#0b5486;
}
*{box-sizing:border-box;margin:0;padding:0}
html,body{width:1200px;height:4612px;overflow:hidden}
body{font-family:"Inter",sans-serif;color:var(--ink);background:var(--bg);position:relative}
.serif{font-family:"Playfair Display",serif}

.nav{height:75px;display:flex;align-items:center;justify-content:center;position:relative;background:#f8fafc}
.nav ul{display:flex;gap:30px;list-style:none;font-size:14px;color:var(--ink)}
.nav .cta{position:absolute;right:30px;top:16px;height:44px;width:192px;border-radius:8px;background:linear-gradient(90deg,var(--blue),var(--cyan));color:#fff;font-size:14px;font-weight:600;display:flex;align-items:center;justify-content:center;gap:8px}

.hero{position:relative;height:675px;background:linear-gradient(100deg,#0e5a86 0%,#1b6f95 35%,#4b8aa0 60%,#2a98b8 80%,#1aa3c4 100%);color:#fff;overflow:hidden}
.hero .photo{position:absolute;inset:0}
.hero .tag{position:absolute;left:30px;top:70px;background:rgba(255,255,255,.18);border:1px solid rgba(255,255,255,.35);border-radius:20px;padding:6px 14px;font-size:12px;font-weight:600}
.hero h1{position:absolute;left:30px;top:125px;font-size:68px;line-height:66px;font-weight:700}
.hero p{position:absolute;left:30px;top:290px;width:700px;font-size:21px;line-height:30px}
.chips{position:absolute;left:30px;top:412px;width:620px;display:flex;flex-wrap:wrap;gap:14px 16px}
.chip{display:flex;align-items:center;gap:8px;background:rgba(255,255,255,.18);border:1px solid rgba(255,255,255,.35);border-radius:8px;padding:9px 14px;font-size:14px;font-weight:600}
.hero .btns{position:absolute;left:30px;top:550px;display:flex;gap:16px}
.btn-p{width:220px;height:52px;border-radius:8px;background:linear-gradient(90deg,var(--blue),var(--cyan));display:flex;align-items:center;justify-content:center;gap:8px;font-weight:600;font-size:16px}
.btn-w{width:208px;height:52px;border-radius:8px;background:#fff;color:var(--blue);display:flex;align-items:center;justify-content:center;font-weight:600;font-size:16px}
.scroll{position:absolute;left:600px;top:608px;width:22px;height:34px;border:2px solid rgba(255,255,255,.7);border-radius:12px}

.sec-head{text-align:center}
.sec-head h2{font-size:46px;font-weight:700}
.sec-head p{margin-top:18px;color:var(--muted);font-size:18px}

.products{position:absolute;top:835px;left:0;width:1200px}
.card{position:absolute;width:556px;height:574px;background:#fff;border-radius:10px;box-shadow:0 6px 24px rgba(15,60,100,.10);overflow:hidden}
.card .img{height:240px}
.card .body{padding:34px 30px 0}
.card .title{display:flex;align-items:center;gap:14px}
.ic{width:34px;height:34px;border-radius:8px;background:linear-gradient(135deg,var(--blue),var(--cyan));display:flex;align-items:center;justify-content:center}
.card h3{font-size:23px;font-weight:700}
.card small{display:block;font-size:12px;color:var(--muted);margin-top:2px}
.card .desc{margin-top:26px;font-size:15px;line-height:25px;color:#3b4856}
.card ul{margin-top:22px;list-style:none;font-size:12.5px;color:var(--muted);line-height:27px}
.card li::before{content:"";display:inline-block;width:6px;height:6px;border-radius:50%;background:var(--blue);margin-right:9px;vertical-align:middle}
.card .more{position:absolute;left:30px;right:30px;bottom:30px;height:36px;border:1.5px solid var(--blue);border-radius:8px;display:flex;align-items:center;justify-content:center;gap:8px;font-size:13px;color:var(--blue);font-weight:500}

.why{position:absolute;top:2345px;left:0;width:1200px}
.feat{position:absolute;width:360px;height:250px;border:1px solid var(--line);border-radius:10px;background:#fff;padding:0 30px}
.feat h4{margin-top:112px;font-size:18px;font-weight:700}
.feat p{margin-top:12px;font-size:14px;line-height:24px;color:var(--muted)}
.blank{position:absolute;left:362px;top:753px;width:476px;height:116px;border-radius:12px;background:#fff;box-shadow:0 10px 34px rgba(15,60,100,.12)}

.contact{position:absolute;top:3385px;left:0;width:1200px}
.form{position:absolute;left:30px;top:193px;width:547px;height:553px;background:#fff;border-radius:10px;box-shadow:0 6px 24px rgba(15,60,100,.08);padding:28px 30px}
.form label{display:block;font-size:13px;font-weight:500;margin-bottom:10px}
.field{height:36px;border:1px solid var(--line);border-radius:6px;font-size:12px;color:#8896a5;padding:10px 12px;margin-bottom:30px}
.field.area{height:140px;margin-bottom:22px}
.send{height:44px;border-radius:8px;background:linear-gradient(90deg,var(--blue),var(--cyan));color:#fff;font-size:14px;font-weight:600;display:flex;align-items:center;justify-content:center;gap:8px}
.info{position:absolute;left:622px;width:548px;background:#fff;border-radius:10px;box-shadow:0 6px 24px rgba(15,60,100,.08);padding:26px 82px}
.info small{font-family:"Playfair Display",serif;font-size:12px;color:var(--muted)}
.info div{margin-top:6px;font-size:17px;font-weight:600}

.footer{position:absolute;top:4221px;left:0;width:1200px;height:391px;background:var(--footer);color:#d6e6f2}
.footer .brand{position:absolute;left:30px;top:58px;font-size:28px;color:#fff;font-weight:700}
.footer .about{position:absolute;left:30px;top:118px;width:400px;font-size:14px;line-height:25px}
.social{position:absolute;left:30px;top:203px;display:flex;gap:16px}
.social span{width:40px;height:40px;border-radius:8px;background:rgba(255,255,255,.12)}
.col{position:absolute;top:62px;font-size:14px}
.col h5{font-family:"Playfair Display",serif;font-size:16px;color:#fff;margin-bottom:18px}
.col p{margin-bottom:11px}
.footer .bottom{position:absolute;left:30px;right:30px;top:340px;display:flex;justify-content:space-between;font-size:12px}
.footer .bottom span+span{margin-left:22px}
</style>
</head>
<body>

<header class="nav">
  <ul><li>Hem</li><li>Pooler</li><li>Pooltak</li><li>Spabad</li><li>Pooldäck</li><li>Om oss</li></ul>
  <div class="cta"><svg width="15" height="15" viewBox="0 0 24 24" fill="none" stroke="#fff" stroke-width="2"><path d="M22 16.9v3a2 2 0 0 1-2.2 2 19.8 19.8 0 0 1-8.6-3.1 19.5 19.5 0 0 1-6-6A19.8 19.8 0 0 1 2.1 4.2 2 2 0 0 1 4.1 2h3a2 2 0 0 1 2 1.7c.1 1 .4 1.9.7 2.8a2 2 0 0 1-.5 2.1L8 9.9a16 16 0 0 0 6 6l1.3-1.3a2 2 0 0 1 2.1-.4c.9.3 1.8.6 2.8.7a2 2 0 0 1 1.7 2z"/></svg>Kontakta oss</div>
</header>

<section class="hero">
  <div class="photo" role="img" aria-label="Modern villa med infinitypool, solstolar och trädäck i kvällsljus"></div>
  <span class="tag">Från dröm till verklighet</span>
  <h1 class="serif">Pooler som förvandlar<br>din trädgård</h1>
  <p>Skapa en exklusiv oas i din trädgård med våra högkvalitativa pooler, pooltak och spabad. Investera i livskvalitet med lösningar som ger avkoppling och glädje året runt.</p>
  <div class="chips">
    <span class="chip"><svg width="14" height="14" viewBox="0 0 24 24" fill="none" stroke="#7ee3f2" stroke-width="2"><circle cx="12" cy="12" r="10"/><path d="M8 12l3 3 5-6"/></svg>Anpassade för nordiskt klimat</span>
    <span class="chip"><svg width="14" height="14" viewBox="0 0 24 24" fill="none" stroke="#7ee3f2" stroke-width="2"><circle cx="12" cy="12" r="10"/><path d="M8 12l3 3 5-6"/></svg>Energieffektiva lösningar</span>
    <span class="chip"><svg width="14" height="14" viewBox="0 0 24 24" fill="none" stroke="#7ee3f2" stroke-width="2"><circle cx="12" cy="12" r="10"/><path d="M8 12l3 3 5-6"/></svg>Komplett installation</span>
  </div>
  <div class="btns">
    <div class="btn-p">Få offert idag <svg width="14" height="14" viewBox="0 0 24 24" fill="none" stroke="#fff" stroke-width="2"><path d="M5 12h14M13 6l6 6-6 6"/></svg></div>
    <div class="btn-w">Se våra pooler</div>
  </div>
  <div class="scroll"></div>
</section>

<section class="products">
  <div class="sec-head"><h2 class="serif">Våra produkter och tjänster</h2><p>Kompletta lösningar för din drömpool - från planering till färdig installation</p></div>

  <article class="card" style="left:30px;top:159px">
    <div class="img" style="background:linear-gradient(135deg,#0a72c0,#0a8fd6);display:flex;align-items:center;justify-content:center">
      <svg width="110" height="80" viewBox="0 0 110 80" fill="none" stroke="rgba(255,255,255,.35)" stroke-width="7" stroke-linecap="round"><path d="M5 15c12-10 22-10 33 0s21 10 33 0 22-10 34 0"/><path d="M5 40c12-10 22-10 33 0s21 10 33 0 22-10 34 0"/><path d="M5 65c12-10 22-10 33 0s21 10 33 0 22-10 34 0"/></svg>
    </div>
    <div class="body">
      <div class="title"><span class="ic"><svg width="18" height="18" viewBox="0 0 24 24" fill="none" stroke="#fff" stroke-width="2"><path d="M2 7c3-2 5-2 7 0s4 2 6 0 4-2 7 0M2 12c3-2 5-2 7 0s4 2 6 0 4-2 7 0M2 17c3-2 5-2 7 0s4 2 6 0 4-2 7 0"/></svg></span><div><h3 class="serif">Pooler</h3><small>Nordvik &amp; Aqualinn</small></div></div>
      <p class="desc">Energieffektiva och hållbara pooler byggda för nordiskt klimat. Från klassiska till infinity-pooler - vi har lösningen för din drömträdgård.</p>
      <ul><li>Nordvikpool med utmärkt värmehållning</li><li>Glasfiberpooler i olika storlekar</li><li>Komplett installationsservice</li></ul>
    </div>
    <div class="more">Läs mer <svg width="12" height="12" viewBox="0 0 24 24" fill="none" stroke="currentColor" stroke-width="2"><path d="M5 12h14M13 6l6 6-6 6"/></svg></div>
  </article>

  <article class="card" style="left:614px;top:159px">
    <div class="img" role="img" aria-label="Pool med teleskopiskt pooltak på trädäck" style="background:linear-gradient(160deg,#a89a88 0%,#4fc0e8 35%,#2aa8e0 65%,#9a8c7a 100%)"></div>
    <div class="body">
      <div class="title"><span class="ic"><svg width="18" height="18" viewBox="0 0 24 24" fill="none" stroke="#fff" stroke-width="2"><path d="M3 10l9-7 9 7v10a1 1 0 0 1-1 1H4a1 1 0 0 1-1-1z"/><path d="M9 21v-7h6v7"/></svg></span><div><h3 class="serif">Pooltak</h3><small>Premium &amp; Solskydd Pro</small></div></div>
      <p class="desc">Förläng badsäsongen och skydda din pool med våra eleganta och energieffektiva pooltak. Säkerhet, stil och komfort i ett.</p>
      <ul><li>Förlänger badsäsongen avsevärt</li><li>Energibesparing upp till 70%</li><li>Elegant design i olika modeller</li></ul>
    </div>
    <div class="more">Läs mer <svg width="12" height="12" viewBox="0 0 24 24" fill="none" stroke="currentColor" stroke-width="2"><path d="M5 12h14M13 6l6 6-6 6"/></svg></div>
  </article>

  <article class="card" style="left:30px;top:762px">
    <div class="img" role="img" aria-label="Upplyst spabad utomhus i kvällsmörker med ånga" style="background:linear-gradient(180deg,#1d2f3c 0%,#2d4a5a 50%,#4fa6c8 75%,#6a5a4a 100%)"></div>
    <div class="body">
      <div class="title"><span class="ic"><svg width="18" height="18" viewBox="0 0 24 24" fill="none" stroke="#fff" stroke-width="2"><path d="M12 3v4M12 17v4M3 12h4M17 12h4M6 6l2.5 2.5M15.5 15.5L18 18M6 18l2.5-2.5M15.5 8.5L18 6"/></svg></span><div><h3 class="serif">Spabad &amp; Swimspa</h3><small>Premium-kvalitet</small></div></div>
      <p class="desc">Upplev total avkoppling året runt med våra lyxiga spabad. Perfekt för motion, rehabilitering eller bara ren njutning.</p>
      <ul><li>Högkvalitativa jets och massage</li><li>Energieffektiv drift</li><li>Swimspa för träning och motion</li></ul>
    </div>
    <div class="more">Läs mer <svg width="12" height="12" viewBox="0 0 24 24" fill="none" stroke="currentColor" stroke-width="2"><path d="M5 12h14M13 6l6 6-6 6"/></svg></div>
  </article>

  <article class="card" style="left:614px;top:762px">
    <div class="img" role="img" aria-label="Pooldäck i kompositmaterial i varm träton" style="background:linear-gradient(180deg,#c9a27e,#b88a63 55%,#c59a74)"></div>
    <div class="body">
      <div class="title"><span class="ic"><svg width="18" height="18" viewBox="0 0 24 24" fill="none" stroke="#fff" stroke-width="2"><rect x="5" y="3" width="14" height="18" rx="1"/><path d="M9 7h2M13 7h2M9 11h2M13 11h2M9 15h2M13 15h2"/></svg></span><div><h3 class="serif">Pooldäck</h3><small>Premium kompositmaterial</small></div></div>
      <p class="desc">Skapa den perfekta poolmiljön med våra stilrena och underhållsfria pooldäck. Hållbara material som tål nordiskt väder.</p>
      <ul><li>Minimalt underhåll krävs</li><li>Slitstark och halkfri yta</li><li>Skräddarsydd design</li></ul>
    </div>
    <div class="more">Läs mer <svg width="12" height="12" viewBox="0 0 24 24" fill="none" stroke="currentColor" stroke-width="2"><path d="M5 12h14M13 6l6 6-6 6"/></svg></div>
  </article>
</section>

<section class="why">
  <div class="sec-head"><h2 class="serif">Varför välja Kalmenstrand?</h2><p>Vi förverkligar pooldrömmar med kvalitet, expertis och passion för det vi gör</p></div>
  <div class="feat" style="left:30px;top:160px"><h4 class="serif">Kvalitet &amp; Säkerhet</h4><p>Endast högkvalitativa material och säkerhetstestade produkter som tål nordiskt klimat.</p></div>
  <div class="feat" style="left:420px;top:160px"><h4 class="serif">Expertis &amp; Erfarenhet</h4><p>Över 20 års erfarenhet av poolinstallationer. Vi guidar dig hela vägen från idé till färdig pool.</p></div>
  <div class="feat" style="left:810px;top:160px"><h4 class="serif">Personlig Service</h4><p>Dedikerad rådgivning och skräddarsydda lösningar anpassade efter dina önskemål och behov.</p></div>
  <div class="feat" style="left:30px;top:441px"><h4 class="serif">Hållbarhet</h4><p>Energieffektiva pooler och tillbehör som minimerar miljöpåverkan och sänker driftskostnader.</p></div>
  <div class="feat" style="left:420px;top:441px"><h4 class="serif">Komplett Service</h4><p>Från planering och installation till underhåll och service - vi tar hand om allt.</p></div>
  <div class="feat" style="left:810px;top:441px"><h4 class="serif">Värdehöjande</h4><p>En pool från Kalmenstrand är en investering som höjer värdet på din fastighet.</p></div>
  <div class="blank"></div>
</section>

<section class="contact">
  <div class="sec-head"><h2 class="serif">Kontakta oss idag</h2><p style="width:660px;margin:18px auto 0;line-height:27px">Låt oss hjälpa dig att förverkliga din pooldröm. Vi ger dig en kostnadsfri konsultation.</p></div>
  <form class="form">
    <label>Namn *</label><div class="field">Ditt namn</div>
    <label>E-post *</label><div class="field">din@email.se</div>
    <label>Telefon</label><div class="field">+46 123 456 789</div>
    <label>Meddelande *</label><div class="field area">Berätta om din pooldröm...</div>
    <div class="send"><svg width="14" height="14" viewBox="0 0 24 24" fill="none" stroke="#fff" stroke-width="2"><path d="M22 2L11 13M22 2l-7 20-4-9-9-4z"/></svg>Skicka meddelande</div>
  </form>
  <div class="info" style="top:193px;height:95px"><small>Telefon</small><div>+46 123 456 789</div></div>
  <div class="info" style="top:309px;height:94px"><small>E-post</small><div>info@kalmenstrand.se</div></div>
  <div class="info" style="top:424px;height:97px"><small>Besök oss</small><div>Showroom efter bokning</div></div>
  <div class="info" style="top:549px;height:184px"></div>
</section>

<footer class="footer">
  <div class="brand serif">Kalmenstrand</div>
  <p class="about">Från dröm till verklighet. Vi skapar exklusiva pooler och spabad som förvandlar din trädgård till en plats för livskvalitet och glädje.</p>
  <div class="social"><span></span><span></span><span></span></div>
  <div class="col" style="left:504px"><h5>Produkter</h5><p>Pooler</p><p>Pooltak</p><p>Spabad</p><p>Pooldäck</p></div>
  <div class="col" style="left:741px"><h5>Företag</h5><p>Om oss</p><p>Kontakt</p><p>Våra projekt</p><p>Karriär</p></div>
  <div class="col" style="left:978px"><h5>Support</h5><p>Kundservice</p><p>Vanliga frågor</p><p>Installation</p><p>Underhåll</p></div>
  <div class="bottom"><span>© 2025 Kalmenstrand. Alla rättigheter förbehållna.</span><div><span>Integritetspolicy</span><span>Användarvillkor</span><span>Cookies</span></div></div>
</footer>

</body>
</html>
```